New modern business card design

To design a brand new business card that's clean & modern in terms of layout.
I have attached our company logo and also basic information regarding what is needed on the card that also needs to be editable.

Target Market(s)

motor trade

Contact Information for Business Card

logo, name, title, tel, mob, email, address, www, all information is in the word.doc file

Requirements
Must have
• white background
Nice to have
• Nice clean font

```html
<!DOCTYPE html>
<html lang="en">
<head>
<meta charset="utf-8">
<title>Daniel Marsh – Business Card</title>
<link rel="stylesheet" href="https://fonts.googleapis.com/css2?family=Open+Sans:wght@400;600&display=swap">
<style>
  :root {
    --backdrop: #e4e4e2;
    --card-light: #f2f2f2;
    --card-mid: #dcdcdc;
    --card-dark: #cfcfcf;
    --name-white: #ffffff;
    --rule-grey: #9a9a9a;
    --text-dark: #3a3a3a;
    --text-body: #2e2e2e;
    --icon-blue: #2b68ad;
    --mark-faint: rgba(255, 255, 255, 0.6);
  }
  * { box-sizing: border-box; margin: 0; padding: 0; }
  html, body {
    width: 1200px; height: 800px; overflow: hidden;
    background: var(--backdrop);
    font-family: "Open Sans", Arial, sans-serif;
  }
  .canvas {
    position: relative; width: 1200px; height: 800px;
    display: flex; align-items: center; justify-content: center;
  }
  .business-card {
    position: relative; width: 900px; height: 520px;
    border-radius: 36px;
    background: linear-gradient(115deg, var(--card-dark) 0%, var(--card-mid) 35%, var(--card-light) 75%, #f7f7f7 100%);
    box-shadow: 0 18px 40px rgba(0,0,0,0.12), 0 2px 6px rgba(0,0,0,0.08);
    overflow: hidden;
  }
  .identity { position: absolute; left: 0; top: 62px; }
  .person-name {
    padding-left: 48px;
    font-size: 60px; font-weight: 400; letter-spacing: 0.5px;
    color: var(--name-white);
    text-shadow: 0 1px 2px rgba(0,0,0,0.08);
    line-height: 1.1;
  }
  .name-rule {
    width: 560px; height: 3px; margin-top: 6px;
    background: linear-gradient(90deg, var(--rule-grey) 0%, var(--rule-grey) 70%, rgba(154,154,154,0) 100%);
  }
  .person-title {
    padding-left: 48px; margin-top: 6px;
    font-size: 26px; font-weight: 600; color: var(--text-dark);
  }
  .company-mark {
    position: absolute; left: 40px; bottom: 30px;
    font-size: 190px; font-weight: 600; line-height: 1;
    color: var(--mark-faint); letter-spacing: 4px;
  }
  .contact-list {
    position: absolute; right: 44px; top: 218px;
    list-style: none;
    display: flex; flex-direction: column; gap: 30px;
  }
  .contact-item {
    display: flex; align-items: center; justify-content: flex-end; gap: 18px;
    font-size: 21px; color: var(--text-body); text-align: right; line-height: 1.2;
  }
  .contact-item.web { font-weight: 600; }
  .contact-icon {
    flex: none; width: 36px; height: 36px; border-radius: 50%;
    background: var(--icon-blue);
    display: flex; align-items: center; justify-content: center;
  }
  .contact-icon svg { width: 20px; height: 20px; fill: #fff; }
</style>
</head>
<body>
<main class="canvas">
  <article class="business-card">
    <header class="identity">
      <h1 class="person-name">Daniel Marsh</h1>
      <div class="name-rule"></div>
      <p class="person-title">General Manager</p>
    </header>

    <div class="company-mark" aria-label="Keyway Extract">KE</div>

    <ul class="contact-list">
      <li class="contact-item phone">
        <span>07700 900 418 - 0161 496 0721</span>
        <span class="contact-icon"><svg viewBox="0 0 24 24"><path d="M6.6 10.8c1.4 2.8 3.8 5.1 6.6 6.6l2.2-2.2c.3-.3.7-.4 1-.2 1.1.4 2.3.6 3.6.6.6 0 1 .4 1 1V20c0 .6-.4 1-1 1C10.6 21 3 13.4 3 4c0-.6.4-1 1-1h3.5c.6 0 1 .4 1 1 0 1.3.2 2.5.6 3.6.1.3 0 .7-.2 1L6.6 10.8z"/></svg></span>
      </li>
      <li class="contact-item address">
        <span>Carver Street. Denton<br>Manchester M34 2QT</span>
        <span class="contact-icon"><svg viewBox="0 0 24 24"><path d="M12 2C8.1 2 5 5.1 5 9c0 5.2 7 13 7 13s7-7.8 7-13c0-3.9-3.1-7-7-7zm0 9.5c-1.4 0-2.5-1.1-2.5-2.5S10.6 6.5 12 6.5s2.5 1.1 2.5 2.5-1.1 2.5-2.5 2.5z"/></svg></span>
      </li>
      <li class="contact-item email">
        <span>dmarsh@keyway-extract.co.uk</span>
        <span class="contact-icon"><svg viewBox="0 0 24 24"><path d="M3 5h18v14H3V5zm2 2v.4l7 4.6 7-4.6V7H5zm14 2.8-7 4.6-7-4.6V17h14V9.8z"/></svg></span>
      </li>
      <li class="contact-item web">
        <span>www.keyway-extract.co.uk</span>
        <span class="contact-icon"><svg viewBox="0 0 24 24"><path d="M12 2a10 10 0 1 0 0 20 10 10 0 0 0 0-20zm6.9 6h-2.9a15 15 0 0 0-1.3-3.6A8 8 0 0 1 18.9 8zM12 4c.8 1.1 1.5 2.5 1.9 4h-3.8c.4-1.5 1.1-2.9 1.9-4zM4.3 14a8 8 0 0 1 0-4h3.3a16 16 0 0 0 0 4H4.3zm.8 2h2.9c.3 1.3.8 2.5 1.3 3.6A8 8 0 0 1 5.1 16zM8 8H5.1a8 8 0 0 1 4.2-3.6C8.8 5.5 8.3 6.7 8 8zm4 12c-.8-1.1-1.5-2.5-1.9-4h3.8c-.4 1.5-1.1 2.9-1.9 4zm2.3-6H9.7a14 14 0 0 1 0-4h4.6a14 14 0 0 1 0 4zm.4 5.6c.5-1.1 1-2.3 1.3-3.6h2.9a8 8 0 0 1-4.2 3.6zm1.7-5.6a16 16 0 0 0 0-4h3.3a8 8 0 0 1 0 4h-3.3z"/></svg></span>
      </li>
    </ul>
  </article>
</main>
</body>
</html>
```